Spirituality Supplement Company Needs A Product Label Design

We are a spirituality company, blog, supplement, company. Our initial product is a supplement that helps with creativity, resilence, and immunity.

We would like to see designs that incorporate a cool design for our product label. The final design should communicate mystical, informed, reassuring, knowledgeable, guiding, wisdom. We attached a picture of our logo. However, I am looking for a more simple and more eye catching design for the logo. You can use the logo attached as a template or to get ideas. We want you to modify our logo for this product design for our supplement to make it more simple and eye catching. Our tagline is Free Your Mind

The ingredients we will have on our supplement is Lions Mane, Reishi, and Turkey Tail mushrooms.

it will be 2 and a half inches width and 10 inches at length. the product label will be on a dark amber glass bottle. (see attached image on post)

Target Market(s)

The driving desires for our consumers are inner power and understanding. Our consumers have a thirst for knowledge and self transformation. Our consumers are into philosophy. Our goal is to show them the path to wisdom.

Our customers primary drives are wisdom, intelligence, expertise, information, influence, transformation, knowledge, vision, belief, and discovery.

Their primary fears are consequences, stagnation, ignorance, doubt, uncertainty, insanity, powerlessness, misinformation, inaccuracy.

Requirements
Must have
• Ingredients labeled. Lions Mane, Reishi, and Turkey Tail Mushroom.
Nice to have
• To show the supplement is promoting Creativity, Resilence, and Immunity.

mind, heart, and body.

I prefer more boldness than elegance. More Playful than serious, more modern than traditional, more personable than professional, more masculine than feminine , more colorful than conservative.

Our mission statement which is, Our mission is to help self actualizing individuals to discover themselves.

It would also be cool if it can look psychedelic.

have the organic, non gmo, 100% natural, vegan, gluten free symbols on product label.

```html
<!DOCTYPE html>
<html lang="en">
<head>
<meta charset="UTF-8">
<title>Quiet Ember – Mushroom Food Supplement Label</title>
<link href="https://fonts.googleapis.com/css2?family=IM+Fell+English&family=IM+Fell+English+SC&display=swap" rel="stylesheet">
<style>
  :root {
    --page-bg: #ececec;
    --label-black: #050404;
    --cream: #f1dfae;
    --gold: #b08a3e;
    --ember-red: #c0301c;
    --deep-red: #5a0c08;
    --orange: #d2561c;
    --leaf-green: #6f8a1e;
    --violet: #4b2a7a;
  }
  * { box-sizing: border-box; margin: 0; padding: 0; }
  html, body {
    width: 1200px;
    height: 1200px;
    overflow: hidden;
    background: var(--page-bg);
  }
  .canvas {
    position: relative;
    width: 1200px;
    height: 1200px;
  }
  .label {
    position: absolute;
    left: 50px;
    top: 128px;
    width: 1100px;
    height: 940px;
    background: var(--label-black);
    overflow: hidden;
  }
  .artwork {
    position: absolute;
    top: 0;
    height: 100%;
  }
  .artwork--left {
    left: 0;
    width: 360px;
    background:
      radial-gradient(ellipse 60% 22% at 45% 8%, rgba(210, 86, 28, 0.85), transparent 70%),
      radial-gradient(ellipse 50% 18% at 70% 16%, rgba(111, 138, 30, 0.6), transparent 70%),
      radial-gradient(ellipse 55% 40% at 20% 45%, rgba(192, 48, 28, 0.75), transparent 75%),
      radial-gradient(ellipse 45% 35% at 25% 85%, rgba(90, 12, 8, 0.9), transparent 75%),
      linear-gradient(90deg, rgba(90, 12, 8, 0.7), transparent 95%);
  }
  .artwork--right {
    right: 0;
    width: 320px;
    background:
      radial-gradient(ellipse 45% 18% at 60% 6%, rgba(111, 138, 30, 0.65), transparent 70%),
      radial-gradient(ellipse 35% 20% at 80% 25%, rgba(75, 42, 122, 0.6), transparent 70%),
      radial-gradient(ellipse 50% 30% at 45% 55%, rgba(210, 86, 28, 0.75), transparent 75%),
      radial-gradient(ellipse 45% 30% at 80% 80%, rgba(192, 48, 28, 0.7), transparent 75%),
      linear-gradient(270deg, rgba(90, 12, 8, 0.65), transparent 95%);
  }
  .benefits {
    position: absolute;
    top: 92px;
    left: 0;
    width: 100%;
    text-align: center;
    font-family: "IM Fell English SC", serif;
    font-size: 38px;
    color: var(--cream);
    letter-spacing: 0.3px;
  }
  .brand-emblem {
    position: absolute;
    left: 309px;
    top: 216px;
    width: 500px;
    height: 500px;
    border: 3px solid var(--gold);
    border-radius: 50%;
    background: radial-gradient(circle, #1a1108 0%, var(--label-black) 75%);
    display: flex;
    align-items: center;
    justify-content: center;
  }
  .brand-name {
    font-family: "IM Fell English SC", serif;
    font-size: 66px;
    line-height: 1.1;
    color: var(--ember-red);
    letter-spacing: 6px;
    text-align: center;
  }
  .product-type {
    position: absolute;
    top: 770px;
    left: 0;
    width: 100%;
    text-align: center;
    font-family: "IM Fell English SC", serif;
    font-size: 38px;
    color: var(--cream);
  }
  .ingredients {
    position: absolute;
    top: 828px;
    left: 0;
    width: 100%;
    text-align: center;
    font-family: "IM Fell English", serif;
    font-size: 35px;
    color: var(--cream);
  }
</style>
</head>
<body>
  <main class="canvas">
    <section class="label">
      <div class="artwork artwork--left" role="img" aria-label="Psychedelic fractal artwork in reds, oranges and greens"></div>
      <div class="artwork artwork--right" role="img" aria-label="Psychedelic fractal artwork in reds, oranges, greens and violet"></div>

      <p class="benefits">PROMOTES CREATIVITY, RESILIENCE &amp; IMMUNITY</p>

      <div class="brand-emblem">
        <span class="brand-name">QUIET<br>EMBER</span>
      </div>

      <p class="product-type">FOOD SUPPLEMENT</p>
      <p class="ingredients">Contains Lion’s Mare, Reishi and Turkey Tail Mushroom</p>
    </section>
  </main>
</body>
</html>
```